Branding product image: TOMBEL (Golden Papaya) in Plastic Cup (Ready to Eat)

The product is sliced Fruit in Light syrup
Flavour: TOMBEL (Golden Papaya)
The temporary product name: TOMBEL
I want the product design to be something 'fun', 'natural', and 'colourful'
The design concept could be anything depends on your imagination, but it must be eye catchy and attractive.
Basically, I want you to be creative in designing the logo and the overall graphic design for the label.
The measurement is 20 cm (Length) x 6,5 cm (Height)
The target customers are young and health conscious audiences (10 years - 65 years old).
Create something different. Something extraordinary.
Brief summary about the fruit:
This fruit only grows in certain part of the world. It grows in mountain area that is in tropical climate. The fruit flesh has a yellowish-golden color. It has an extraordinary taste (unlike normal papaya) and it suits very well with any dishes from cold appetizer, white/ red meat, desserts, and cocktails.
I need a packaging design for Fruit Cup productThe product is sliced Fruit in Light syrup.There will be various flavours i.e. apple, lychee, peach, papaya, etc.However, you may design the product using one sample flavour (i.e. papaya) first, as the designs of other flavours could be adjusted afterwards.The temporary product name is: RICCANAI want the product design to be something 'fun', 'natural', and 'colourful'.The design concept could be anything depends on your imagination. Basically, I want you to be creative in designing the logo and the overall graphic design for the label. - Create something different. Something extraordinary -Additional:The measurement is 20cm (Length) x 5cm (Height).The target customers are young audiences (10 years - 35 years old).The product design must stand out in the supermarket shelf.It must be eye catchy and attractive.Thank you,Harold-PLEASE REFER TO DESIGN SAMPLE ATTACHED TO HAVE A BETTER UNDERSTANDING FOR THE PRODUCT CONCEPT- Added Wednesday, September 17, 2014
Project Deadline Extended Reason: Haven't found a good design. Added Friday, September 19, 2014
Project Deadline Extended Reason: Need more time for designers to finalize and perfect the design.Thank you,Harold Added Monday, September 29, 2014
Project Deadline Extended Reason: I haven't found a great design yet. Added Tuesday, February 24, 2015
Reason: Getting better designs now. Still Open to new ideas while refining the latest designs from some designers.
Please do your best in submitting other great designs!

```html
<!DOCTYPE html>
<html lang="en">
<head>
<meta charset="utf-8">
<title>LUPEDOS Fruit Cup – Apple Label</title>
<link rel="stylesheet" href="https://fonts.googleapis.com/css2?family=Londrina+Solid:wght@900&family=Fredoka:wght@600;700&display=swap">
<style>
  :root {
    --label-white: #ffffff;
    --stripe-green: #7ed83c;
    --panel-blue: #6bbfe3;
    --ink-navy: #1b2d6b;
    --photo-red: #b5121b;
    --photo-deep: #7a0c13;
    --photo-light: #d8303a;
  }
  html, body {
    margin: 0;
    padding: 0;
    overflow: hidden;
    background: var(--label-white);
  }
  .label {
    position: relative;
    width: 1200px;
    height: 300px;
    overflow: hidden;
    background: var(--label-white);
  }
  .stripe {
    position: absolute;
    left: 0;
    width: 1200px;
    background: var(--stripe-green);
  }
  .stripe--top { top: 42px; height: 32px; }
  .stripe--main { top: 87px; height: 125px; }
  .stripe--lower { top: 228px; height: 13px; }
  .stripe--base { top: 256px; height: 14px; }

  .fruit-photo {
    position: absolute;
    left: 492px;
    top: 8px;
    width: 246px;
    height: 292px;
    border-radius: 40px 40px 0 0;
    background: radial-gradient(ellipse at 45% 40%, var(--photo-light) 0%, var(--photo-red) 55%, var(--photo-deep) 100%);
  }
  .flavour-badge {
    position: absolute;
    left: 0;
    top: 0;
    width: 1200px;
    height: 300px;
  }
  .flavour-name {
    position: absolute;
    left: 500px;
    width: 230px;
    top: 244px;
    margin: 0;
    text-align: center;
    font-family: "Fredoka", sans-serif;
    font-weight: 700;
    font-size: 36px;
    line-height: 44px;
    color: var(--label-white);
  }
  .product-type {
    position: absolute;
    left: 714px;
    top: 41px;
    margin: 0;
    font-family: "Fredoka", sans-serif;
    font-weight: 700;
    font-size: 25px;
    line-height: 34px;
    color: var(--label-white);
  }
  .brand-name {
    position: absolute;
    left: 398px;
    top: 80px;
    margin: 0;
    font-family: "Londrina Solid", sans-serif;
    font-weight: 900;
    font-size: 140px;
    line-height: 1;
    color: var(--label-white);
    transform: scaleX(0.89);
    transform-origin: left top;
    white-space: nowrap;
  }
  .info-panel {
    position: absolute;
    left: 925px;
    top: 0;
    width: 187px;
    height: 300px;
    background: var(--panel-blue);
  }
  .product-description {
    position: absolute;
    left: 0;
    top: 54px;
    width: 187px;
    margin: 0;
    text-align: center;
    font-family: "Fredoka", sans-serif;
    font-weight: 700;
    font-size: 50px;
    color: var(--ink-navy);
    text-transform: uppercase;
  }
  .product-description .line {
    display: block;
    height: 48px;
    line-height: 48px;
  }
  .product-description .small-word {
    font-size: 18px;
    line-height: 1;
    text-transform: none;
  }
</style>
</head>
<body>
<div class="label">
  <div class="stripe stripe--top"></div>
  <div class="stripe stripe--main"></div>
  <div class="stripe stripe--lower"></div>
  <div class="stripe stripe--base"></div>

  <div class="fruit-photo" role="img" aria-label="Product photograph: a shiny red apple with a green leaf on its stem"></div>

  <svg class="flavour-badge" viewBox="0 0 1200 300" aria-hidden="true">
    <circle cx="615" cy="365" r="128" fill="var(--panel-blue)"/>
  </svg>
  <p class="flavour-name">APPLE</p>

  <p class="product-type">Fruit cup</p>
  <h1 class="brand-name">LUPEDOS</h1>

  <div class="info-panel">
    <p class="product-description">
      <span class="line">Sliced</span>
      <span class="line">Fruit<span class="small-word">in</span></span>
      <span class="line">Light</span>
      <span class="line">Syrup</span>
    </p>
  </div>
</div>
</body>
</html>
```